8.5 x 11 Two Sided Flyer with our coffee descriptions/images

See www.BrindleKettle.com for elements and design look.

I have need to put all of our coffee bags onto a flyer with a brief description of each.

The header title should have the logo and the words Brindle Kettle Co.
Underneath a paragraph that states:
Located in the hills of Paulding County, Georgia, our small-batch craft coffees are freshly-roasted from responsibly sourced beans to ensure premium quality and taste. Retail: $19.95 for a full 16 oz. pound of freshly roasted ground or whole bean coffee. Wake up to better coffee with Brindle Kettle!

Then below, a small image of each of the coffees with their descriptions. SEE THE BOTTOM OF THIS PROJECT DESCRIPTION

At the very bottom, the url - www.BrindleKettle.com

The coffees should remain in the order provided.

FELICE SERA - Italian Roast
Hints of Dark Chocolate and Raspberry

From the hillsides of Tuscany to the waters of the Amalfi coast to the architecture of Rome, Italy is one of the most beautiful countries in the world.

Whether it’s high fashion and fast cars or fine wine an extra-virgin olive oil, the word “Italian” is synonymous with quality and the enjoyment of life’s finer things. As an old Italian proverb urges, “If you cannot live longer, live deeper.”

Following in the footsteps of his great-grandfather Enzo, Marco Dellatesta is a second generation Italian-American entrepreneur with a passion for living life to the fullest. A successful businessman, Enzo had a steel-like work ethic that fueled his vision. He saw opportunity, and through hard work and determination, would soon see it thrive. Volumes could be written about all that Italians like Enzo have contributed to the world.

When you walk the streets of Italy, you’ll also discover that Italians know no strangers. If you take the opportunity to visit one of the many cafes in any Italian city, you’ll be greeted with warm and sincere hospitality. “Felice Sera!” You’ll be offered gelato, a cannoli, likely a robust cup of caffé. Italians love their coffee almost as much as their wine. By the time you regretfully move on, you will be among friends.

To this end, we proclaim “Felice Sera,” and invite you to take a moment to live deeply and enjoy this robust Italian roast with us, your new friends, before you tackle life’s newest adventure.

Ciao.

ARCADIA - 4 X Caffeine - Sumatran & Indian

Arcadia: The afterlife where the chosen, the righteous, and the heroic indulge in everlasting pleasure. Compare to Grave Oath coffee.

This propriety blend is shown to possess more than four times the caffeine content of your standard cup. Experience the divinely bold coffee cup that results from exotic, dark-roasted Sumatran and Indian beans, where earthy notes and mild acidity balance to produce a rich, heavy body.

Why wish for death when you can experience Arcadia?

BANNER - Medium-Dark Roast Blend - Africa & Central America
Bold and hearty with notes of cocoa

Banner Blend celebrates the “melting pot” quality that gives our United States vitality.

The Banner Blend is intentionally mixed and roasted to be bold, the way we’d like all coffee to be. It begins with a refreshing balance of the best beans from Central America and Africa, and ends with a flavor only roasting in America can provide.

The specific flavors of this blend will vary from season to season, as all good coffees do, with coffee farming and cultivation ever changing throughout the year. But the essence of American craftsmanship will always ring true in this blended roast.

We wanted a coffee dedicated to American ideals. We wanted a drink worthy of our Founding Fathers; a drink we’d gladly brew in the great American tradition of consuming coffee—going all the way back to the Boston Tea Party.
After countless roasting sessions and tasting cup after cup of coffee, we settled on a combination of medium-dark roasted and dark roasted beans (we suspect James Whitlow made his the same way). The resulting blend is technically known as a melange, but we still call it a blend; one in keeping with the diverse and blended nature of our favorite constitutional republic.

DRIFTER - Decaf Medium-Dark Roast - Guatemala
Herbal and sweet with notes of caramel

Wind down with our fragrant and luscious decaf. Its complex aroma and smooth, sweet taste are a great way to start your decaffeinated day. Pairs well with chocolate or sugar cookies. Try it iced with your favorite syrup and whipped cream for a decadent, soothing indulgence.

Sleep easy knowing Drifter is always Alpine Brook Processed and never chemically decaffeinated.

TIMBERLINE - Medium Roast - Ethiopia
Bright and vibrant with notes of blueberry

The first TIMBERLINE Act of 1862 gave plots of land to farmers in the federally-owned properties of the West. The kinds of people who took advantage of this offer had a unique combination of traits.

On one hand, they were adventurous enough to leave the “settled” lands and move to the frontier. On the other hand, these were people looking for homes. They wanted to settle down, start families, and send down deep roots.

The Timberline Roast honors that curious combination of traits. It’s a member of the Brindle Kettle family, so you know it’s not going to be the coffee-as-usual you might expect from other roasters. It’s dauntless in that way.

But it’s also comfortable and cordial. The Timberline Roast just might put the word “hearth” in mind. Or “front porch.” That works too.

Vibrant and spirited, with citrus acidity and a smooth finish, the Timberline Roast is deliciously versatile. It wakes you up in the morning and facilitates your after-dinner conversation.

Timberline Roast brews up a golden brown, but it’s not overpowering. In fact, you might call it hospitable, because it always makes room for sugar and cream – or flavored syrup, if that’s your thing.

Even if you prefer a darker roast for yourself, the Timberline Roast makes a great addition to your home or business pantry to ensure you always have a satisfying, rich cup of coffee right in the comfort zone of most coffee drinkers.

WAYFARER - Medium-Dark Roast - Bolivia
Sweet and citric with notes of almond

America has always had more than its fair share of pioneers. From Daniel Boone to Jimi Hendrix to Steve Jobs, there’s something in our DNA that drives us to do things a little differently.

But pioneers are nothing if not practical. Because a useless innovation is in many ways worse than a mediocre commonplace.

That’s why we named our medium-dark roast the Wayfarer. It’s bold, for sure. But it’s not brash. It’s for the pioneer in all of us—with one eye on the frontier, and the other on taking care of business.

Velvety and rich, with notes of tree nuts and cocoa, the versatile Wayfarer Roast strikes out into the unexplored territory of the bold roast profiles.

The medium-dark Wayfarer Roast plays double duty. A “Goldilocks” blend that’s not too dark or too light, its flexible flavor profile goes well with foods both savory and sweet.

If you opt for fried bacon and scrambled eggs for breakfast over a bowl of cold cereal or a bagel, you’ll find the Wayfarer Roast’s notes of earthiness and toasted grain pleasantly accent your rich, savory breakfast.

On the other fork, if you’re looking for a good coffee to drink with your decadent double-decker chocolate cake, you’ll find Wayfarer Roast’s touch of smokiness cuts through and complements your sugary treat.

BONANZA - Dark Roast - Burundi
Chocolatey with notes of cherry

American prospectors made it all the way to the coast. They were never able to shake that pilgrim feeling that there was something even better a little further West… just a bit further on.

When some settlers hunkered down and built houses in the fly-over states, the prospectors kept going. They were looking for gold. But they were really hoping for a dream.

The Bonanza Roast honors that tradition. Going well beyond first crack, our expert roasters take these intrepid beans all the way to oil-coated glory. This is a bean that goes the distance. For people who won’t settle for anything less.

This dark-roasted bean packs a serious punch. Not all beans can stand up to the intense roasting temperatures required to turn a green bean into a lean, mean, caffeine machine.

That’s why our single origin Bonanza Roast utilizes only the most robust beans from the mountains of Central Africa to give you the maximum in bean and roast flavor in one compact package.

But let’s face it. You’re drinking this coffee because you like the complexity and richness that only a dark bean can offer. Sure, this coffee will pair with food. But who cares? This is a coffee you drink on its own. You drink it black.

You listen to music. You light your pipe, your cigar, your fire. This will keep you going. No matter what your prospects.

OUTPOST - Medium-Dark Roast - India, Ethiopia, Brazil
Hearty and nutty with a berry finish

Saddle up with a savory, complex and decadent roast. Perfect for all your favorite espresso drinks! Outpost can also be prepared without an espresso machine. Explore the expansive flavor profile with your preferred brewing method.

Outpost is blended with the finest beans from India, Ethiopia and Brazil. This espresso offers a hearty mouthfeel with a sweet berry finish.

DEREK MOANA’S RIPTIDE - Dark Roast - Brazil, Sumatra, Kenya

“This dark roast is what is I crave from a cup of coffee. Big, full-bodied, and bold. My exotic blend is made from responsibly sourced Brazilian, Sumatran and Kenyan beans. This coffee is the perfect way to embrace a beautiful day. Mahalo!” – Derek Moana

DEREK MOANA’S ROCKET - Medium 2X Caffeine - Sumatra, India
“Rocket is my nickname, because I go fast and head first into what I love. It takes a special coffee to tackle the biggest waves. Be warned this coffee has more than double the caffeine of your standard cup. Responsibly sourced Sumatran & Indian beans bring balance to the scales of flavor and power. This coffee is the perfect way to tackle an epic day. Shoots!” – Derek Moana

Target Market(s)

Grocery buyers

Industry/Entity Type

Grocery

Font styles to use
Serif
Sans Serif

Requirements
Must have
• Uniformity in the size and font styles - pretend it's a catalog
Nice to have
• Elements of brown / gold / black
Should not have
• Do not use bright colors - this is a luxury market and coffee related, does not want bright or neon colors

```html
<!DOCTYPE html>
<html lang="en">
<head>
<meta charset="utf-8">
<title>Brindle Kettle Co. – Coffee Flyer</title>
<link rel="stylesheet" href="https://fonts.googleapis.com/css2?family=Merriweather:wght@400;700&display=swap">
<style>
  :root{
    --backdrop:#ece3d3;
    --paper-top:#f5eed4;
    --paper-bottom:#ecdfae;
    --ink:#2a1a0f;
    --wood-dark:#4a2a14;
    --ring:#8a5a35;
    --bag:#c9a57e;
    --white:#ffffff;
  }
  *{box-sizing:border-box;margin:0;padding:0}
  html,body{width:1200px;height:1200px;overflow:hidden}
  body{background:var(--backdrop);position:relative;font-family:"Merriweather",serif;color:var(--ink)}

  .flyer{position:absolute;top:186px;width:557px;height:720px;overflow:hidden;
    background:linear-gradient(180deg,var(--paper-top) 0%,var(--paper-bottom) 100%)}
  .flyer--front{left:32px}
  .flyer--back{left:629px}

  .flyer__header{position:absolute;left:0;top:0;width:557px;height:110px}
  .brand{position:absolute;top:16px;left:0;width:100%;display:flex;justify-content:center;align-items:center;gap:9px}
  .brand__mark{width:26px;height:26px;border-radius:50%;border:2px solid var(--white)}
  .brand__name{font-weight:700;font-size:17px;color:var(--white);letter-spacing:.5px}

  .intro{position:absolute;left:30px;top:88px;width:497px;text-align:center;font-size:8.9px;line-height:11.8px;font-style:normal}

  .bag{position:absolute;width:80px;height:80px;border-radius:50%;
    background:radial-gradient(circle at 50% 45%,var(--bag) 0%,var(--ring) 62%,var(--wood-dark) 100%)}

  .coffee{position:absolute;text-align:center;font-size:8.9px;line-height:11.8px;color:var(--ink)}
  .coffee__title{font-size:9.6px;font-weight:400;letter-spacing:.2px;line-height:12px}
  .coffee p{margin:0}
  .coffee .left{text-align:left}

  .flyer__beans{position:absolute;left:0;bottom:0;width:557px;height:80px}
  .flyer__url{position:absolute;right:30px;bottom:14px;font-weight:700;font-size:14px;color:var(--white);letter-spacing:.3px}
</style>
</head>
<body>

<!-- FRONT: Felice Sera to Timberline -->
<section class="flyer flyer--front">
  <svg class="flyer__header" viewBox="0 0 557 110" role="img" aria-label="Weathered wood plank header with torn paper edge">
    <defs>
      <linearGradient id="woodA" x1="0" x2="1" y1="0" y2="0">
        <stop offset="0" stop-color="#4a2a14"/><stop offset=".3" stop-color="#8a5a30"/>
        <stop offset=".55" stop-color="#5e3519"/><stop offset=".8" stop-color="#9a6636"/><stop offset="1" stop-color="#4a2a14"/>
      </linearGradient>
    </defs>
    <path fill="url(#woodA)" d="M0 0H557V62L540 70 522 60 505 74 486 64 470 78 452 66 430 72 412 58 394 70 376 62 356 76 338 64 318 72 300 60 282 68 262 62 244 76 226 64 206 70 190 58 170 72 150 62 132 76 112 64 94 70 76 58 58 72 40 62 20 74 0 64Z"/>
  </svg>
  <div class="brand"><span class="brand__mark"></span><span class="brand__name">Brindle Kettle Co.</span></div>

  <p class="intro">Located in the hills of Paulding County, Georgia, our small-batch craft coffees are freshly-roasted from responsibly sourced beans to ensure premium quality and taste. Retail: $19.95 for a full 16 oz. pound of freshly roasted ground or whole bean coffee. Wake up to better coffee with Brindle Kettle!</p>

  <div class="bag" role="img" aria-label="Felice Sera coffee bag photo" style="left:124px;top:128px"></div>
  <div class="bag" role="img" aria-label="Arcadia coffee bag photo" style="left:393px;top:128px"></div>

  <article class="coffee" style="left:14px;top:212px;width:300px">
    <h2 class="coffee__title">FELICE SERA - Italian Roast</h2>
    <p>Hints of Dark Chocolate and Raspberry</p>
    <p class="left">From the hillsides of Tuscany to the waters of the Amalfi coast to the architecture of Rome, Italy is one of the most beautiful countries in the world. Whether it’s high fashion and fast cars or fine wine an extra-virgin olive oil, the word “Italian” is synonymous with quality and the enjoyment of life’s finer things. As an old Italian proverb urges, “If you cannot live longer, live deeper.”</p>
    <p class="left">To this end, we proclaim “Felice Sera,” and invite you to take a moment to live deeply and enjoy this robust Italian roast with us, your new friends, before you tackle life’s newest adventure.</p>
    <p class="left">Ciao.</p>
  </article>

  <article class="coffee" style="left:322px;top:212px;width:224px">
    <h2 class="coffee__title">ARCADIA - 4 X Caffeine - Sumatran &amp; Indian</h2>
    <p>Arcadia: The afterlife where the chosen, the righteous, and the heroic indulge in everlasting pleasure. Compare to Grave Oath coffee.</p>
    <p>This propriety blend is shown to possess more than four times the caffeine content of your standard cup. Experience the divinely bold coffee cup that results from exotic, dark-roasted Sumatran and Indian beans, where earthy notes and mild acidity balance to produce a rich, heavy body.</p>
    <p>Why wish for death when you can experience Arcadia?</p>
  </article>

  <div class="bag" role="img" aria-label="Banner coffee bag photo" style="left:74px;top:380px"></div>
  <div class="bag" role="img" aria-label="Drifter coffee bag photo" style="left:250px;top:380px"></div>
  <div class="bag" role="img" aria-label="Timberline coffee bag photo" style="left:415px;top:380px"></div>

  <article class="coffee" style="left:12px;top:464px;width:204px">
    <h2 class="coffee__title">BANNER - Medium-Dark Roast Blend - Africa &amp; Central America</h2>
    <p>Bold and hearty with notes of cocoa</p>
    <p>Banner Blend celebrates the “melting pot” quality that gives our United States vitality.</p>
    <p>We wanted a coffee dedicated to American ideals. We wanted a drink worthy of our Founding Fathers; a drink we’d gladly brew in the great American tradition of consuming coffee—going all the way back to the Boston Tea Party.</p>
    <p>After countless roasting sessions and tasting cup after cup of coffee, we settled on a combination of medium-dark roasted and dark roasted beans (we suspect James Whitlow made his the same way).</p>
  </article>

  <article class="coffee" style="left:222px;top:464px;width:136px">
    <h2 class="coffee__title">DRIFTER - Decaf Medium-Dark Roast - Guatemala</h2>
    <p>Herbal and sweet with notes of caramel</p>
    <p>Wind down with our fragrant and luscious decaf. Its complex aroma and smooth, sweet taste are a great way to start your decaffeinated day. Pairs well with chocolate or sugar cookies. Try it iced with your favorite syrup and whipped cream for a decadent, soothing indulgence.</p>
  </article>

  <article class="coffee" style="left:366px;top:464px;width:180px">
    <h2 class="coffee__title">TIMBERLINE - Medium Roast - Ethiopia</h2>
    <p>Bright and vibrant with notes of blueberry</p>
    <p>Vibrant and spirited, with citrus acidity and a smooth finish, the Timberline Roast is deliciously versatile.</p>
    <p>Timberline Roast brews up a golden brown, but it’s not overpowering. In fact, you might call it hospitable, because it always makes room for sugar and cream – or flavored syrup, if that’s your thing.</p>
  </article>

  <svg class="flyer__beans" viewBox="0 0 557 80" role="img" aria-label="Photo of roasted coffee beans along the bottom edge">
    <defs>
      <linearGradient id="beansA" x1="0" x2="0" y1="0" y2="1">
        <stop offset="0" stop-color="#6b3a1c" stop-opacity="0"/><stop offset=".4" stop-color="#6b3a1c"/><stop offset="1" stop-color="#2b170b"/>
      </linearGradient>
    </defs>
    <path fill="url(#beansA)" d="M0 28Q60 20 120 34T260 20T400 14T557 22V80H0Z"/>
  </svg>
  <div class="flyer__url">www.BrindleKettle.com</div>
</section>

<!-- BACK: Wayfarer to Rocket -->
<section class="flyer flyer--back">
  <svg class="flyer__header" viewBox="0 0 557 110" role="img" aria-label="Weathered wood plank header with torn paper edge">
    <defs>
      <linearGradient id="woodB" x1="0" x2="1" y1="0" y2="0">
        <stop offset="0" stop-color="#4a2a14"/><stop offset=".3" stop-color="#8a5a30"/>
        <stop offset=".55" stop-color="#5e3519"/><stop offset=".8" stop-color="#9a6636"/><stop offset="1" stop-color="#4a2a14"/>
      </linearGradient>
    </defs>
    <path fill="url(#woodB)" d="M0 0H557V62L540 70 522 60 505 74 486 64 470 78 452 66 430 72 412 58 394 70 376 62 356 76 338 64 318 72 300 60 282 68 262 62 244 76 226 64 206 70 190 58 170 72 150 62 132 76 112 64 94 70 76 58 58 72 40 62 20 74 0 64Z"/>
  </svg>
  <div class="brand"><span class="brand__mark"></span><span class="brand__name">Brindle Kettle Co.</span></div>

  <div class="bag" role="img" aria-label="Wayfarer coffee bag photo" style="left:120px;top:92px"></div>
  <div class="bag" role="img" aria-label="Bonanza coffee bag photo" style="left:381px;top:92px"></div>

  <article class="coffee" style="left:24px;top:178px;width:272px">
    <h2 class="coffee__title">WAYFARER - Medium-Dark Roast - Bolivia</h2>
    <p>Sweet and citric with notes of almond</p>
    <p>Velvety and rich, with notes of tree nuts and cocoa, the versatile Wayfarer Roast strikes out into the unexplored territory of the bold roast profiles.</p>
    <p>The medium-dark Wayfarer Roast plays double duty. A “Goldilocks” blend that’s not too dark or too light, its flexible flavor profile goes well with foods both savory and sweet.</p>
  </article>

  <article class="coffee" style="left:304px;top:178px;width:242px">
    <h2 class="coffee__title">BONANZA - Dark Roast - Burundi</h2>
    <p>Chocolatey with notes of cherry</p>
    <p>This dark-roasted bean packs a serious punch. Not all beans can stand up to the intense roasting temperatures required to turn a green bean into a lean, mean, caffeine machine.</p>
    <p>But let’s face it. You’re drinking this coffee because you like the complexity and richness that only a dark bean can offer. Sure, this coffee will pair with food. But who cares? This is a coffee you drink on its own. You drink it black.</p>
  </article>

  <div class="bag" role="img" aria-label="Outpost coffee bag photo" style="left:70px;top:352px"></div>
  <div class="bag" role="img" aria-label="Derek Moana’s Riptide coffee bag photo" style="left:238px;top:352px"></div>
  <div class="bag" role="img" aria-label="Derek Moana’s Rocket coffee bag photo" style="left:415px;top:352px"></div>

  <article class="coffee" style="left:20px;top:436px;width:180px">
    <h2 class="coffee__title">OUTPOST - Medium-Dark Roast - India, Ethiopia, Brazil</h2>
    <p>Hearty and nutty with a berry finish</p>
    <p class="left">Saddle up with a savory, complex and decadent roast. Perfect for all your favorite espresso drinks! Outpost can also be prepared without an espresso machine. Explore the expansive flavor profile with your preferred brewing method.</p>
    <p class="left">Outpost is blended with the finest beans from India, Ethiopia and Brazil. This espresso offers a hearty mouthfeel with a sweet berry finish.</p>
  </article>

  <article class="coffee" style="left:206px;top:436px;width:164px">
    <h2 class="coffee__title">DEREK MOANA’S RIPTIDE - Dark Roast - Brazil, Sumatra, Kenya</h2>
    <p>“This dark roast is what is I crave from a cup of coffee. Big, full-bodied, and bold. My exotic blend is made from responsibly sourced Brazilian, Sumatran and Kenyan beans. This coffee is the perfect way to embrace a beautiful day. Mahalo!”<br>– Derek Moana</p>
  </article>

  <article class="coffee" style="left:376px;top:436px;width:170px">
    <h2 class="coffee__title">DEREK MOANA’S ROCKET - Medium 2X Caffeine - Sumatra, India</h2>
    <p class="left">“Rocket is my nickname, because I go fast and head first into what I love. It takes a special coffee to tackle the biggest waves. Be warned this coffee has more than double the caffeine of your standard cup. Responsibly sourced Sumatran &amp; Indian beans bring balance to the scales of flavor and power. This coffee is the perfect way to tackle an epic day. Shoots!” – Derek Moana</p>
  </article>

  <svg class="flyer__beans" viewBox="0 0 557 80" role="img" aria-label="Photo of roasted coffee beans along the bottom edge">
    <defs>
      <linearGradient id="beansB" x1="0" x2="0" y1="0" y2="1">
        <stop offset="0" stop-color="#6b3a1c" stop-opacity="0"/><stop offset=".4" stop-color="#6b3a1c"/><stop offset="1" stop-color="#2b170b"/>
      </linearGradient>
    </defs>
    <path fill="url(#beansB)" d="M0 28Q60 20 120 34T260 20T400 14T557 22V80H0Z"/>
  </svg>
  <div class="flyer__url">www.BrindleKettle.com</div>
</section>

</body>
</html>
```